Web landing page design

- Create a Web Design (Uncoded - PSD layout only)

We need a single web page design to promote our service. This page will
acts as a landing page for users and also be utilized in social media
advertising. Please provide us with a cutting edge design. I have attached
a link for what the company is about. In essence we are a photo checking
service which reviews photos for retailers, hotels abd car dealerships to
check everything is good after a service has been performed. Whether it be
a new promotion, cleaning or just checking prices. I am looking for a
design to say that we do many photos and at a very cost effective price
(team based in Mexico)

Link: https://slidewharf.example/view/qT4nRz8LmXcV2pKdHs0w/
*Deadline*
5 days
*Updates*

- The Start Here box needs to look like this:

-Start Here (heading)
-A box for email addresses to be entered
-Then a check box with "Yes, I have read and agree to the Privacy Policy
and agree to receive email marketing from Snapora88'
-A submit button

All of this information needs to be in one box please. And please feel
free to contact me if you have any questions about this.

*Target Market(s)*
Retail business, Merchandising companies, Rental property owners, Car
dealers
Updates

Please can you submit entries. I am just looking for a tidy to a presentation already created. Just needs design touches.

Target Market(s)

Ability for audience to understand concept quickly
Benefits to why to use the product stand out
Technology driven approach

Industry/Entity Type

Retail

Number of Pages Required

1 page

Colors
0792cd

Requirements
Must have
• Clean and modern design

```html
<!DOCTYPE html>
<html lang="en">
<head>
<meta charset="utf-8">
<title>snapora88 — Transform retail execution with a simple photo</title>
<link rel="stylesheet" href="https://fonts.googleapis.com/css2?family=Poppins:wght@600&family=Arimo:wght@400;700&display=swap">
<style>
  :root {
    --brand-blue: #0792cd;
    --stat-blue: #1e9ad6;
    --white: #ffffff;
    --scene-warm: #c98a4a;
    --scene-mid: #5a3a26;
    --scene-dark: #1d1410;
    --bar-bg: rgba(10, 10, 12, 0.55);
    --bar-line: rgba(255, 255, 255, 0.12);
  }
  * { margin: 0; padding: 0; box-sizing: border-box; }
  html, body { width: 1200px; height: 665px; overflow: hidden; background: var(--scene-dark); }
  .landing {
    position: relative;
    width: 1200px;
    height: 665px;
    overflow: hidden;
    font-family: "Arimo", Arial, sans-serif;
    color: var(--white);
  }
  .hero-photo {
    position: absolute;
    inset: 0;
    background:
      radial-gradient(ellipse 320px 240px at 200px 20px, rgba(255, 214, 150, 0.85), transparent 70%),
      radial-gradient(ellipse 260px 420px at 690px 380px, rgba(120, 70, 45, 0.6), transparent 75%),
      linear-gradient(100deg, #4a3024 0%, var(--scene-warm) 22%, var(--scene-mid) 48%, #3a271d 75%, #2a1d16 100%);
  }
  .hero-shade {
    position: absolute;
    inset: 0;
    background: linear-gradient(180deg, rgba(0,0,0,0) 55%, rgba(0,0,0,0.35) 100%);
  }
  .brand {
    position: absolute;
    top: 59px;
    left: 0;
    width: 100%;
    text-align: center;
  }
  .brand-mark {
    display: block;
    width: 58px;
    height: 58px;
    margin: 0 auto;
    border-radius: 50%;
    background: var(--brand-blue);
  }
  .brand-name {
    display: block;
    margin-top: 2px;
    font-family: "Poppins", sans-serif;
    font-weight: 600;
    font-size: 46px;
    line-height: 56px;
    color: var(--white);
    letter-spacing: 0.5px;
  }
  .headline {
    position: absolute;
    top: 222px;
    left: 0;
    width: 100%;
    text-align: center;
    font-family: "Poppins", sans-serif;
    font-weight: 600;
    font-size: 37px;
    line-height: 38px;
    letter-spacing: 0.3px;
  }
  .section-nav {
    position: absolute;
    top: 360px;
    left: 414px;
    display: flex;
    gap: 17px;
  }
  .nav-ring {
    position: relative;
    width: 80px;
    height: 88px;
    display: flex;
    align-items: center;
    justify-content: center;
    color: var(--white);
    text-decoration: none;
    font-size: 11.5px;
  }
  .nav-ring svg { position: absolute; inset: 0; }
  .nav-ring span { position: relative; padding-left: 8px; }
  .stats-bar {
    position: absolute;
    left: 0;
    bottom: 0;
    width: 100%;
    height: 79px;
    background: var(--bar-bg);
    border-top: 1px solid var(--bar-line);
    display: flex;
    justify-content: center;
  }
  .stat {
    width: 183px;
    text-align: center;
    padding-top: 14px;
  }
  .stat + .stat { border-left: 1px solid var(--bar-line); }
  .stat:first-child { width: 233px; padding-left: 50px; }
  .stat:last-child { width: 233px; padding-right: 50px; }
  .stat-value {
    display: block;
    font-weight: 700;
    font-size: 25px;
    line-height: 28px;
    color: var(--stat-blue);
  }
  .stat-label {
    display: block;
    margin-top: 4px;
    font-size: 11.5px;
    line-height: 14px;
  }
</style>
</head>
<body>
<main class="landing">
  <div class="hero-photo" role="img" aria-label="Woman with curly hair smiling at her smartphone on a warm, sunlit city street"></div>
  <div class="hero-shade"></div>

  <header class="brand">
    <span class="brand-mark"></span>
    <span class="brand-name">snapora88</span>
  </header>

  <h1 class="headline">Transform retail execution<br>with a simple photo</h1>

  <nav class="section-nav">
    <a class="nav-ring" href="#about">
      <svg width="80" height="88" viewBox="0 0 80 88"><path d="M40 4 A40 40 0 0 0 24 82" fill="none" stroke="#0792cd" stroke-width="1.6"/><circle cx="44" cy="44" r="36" fill="none" stroke="#fff" stroke-width="1.6"/></svg>
      <span>About</span>
    </a>
    <a class="nav-ring" href="#result">
      <svg width="80" height="88" viewBox="0 0 80 88"><path d="M40 4 A40 40 0 0 0 24 82" fill="none" stroke="#0792cd" stroke-width="1.6"/><circle cx="44" cy="44" r="36" fill="none" stroke="#fff" stroke-width="1.6"/></svg>
      <span>Result</span>
    </a>
    <a class="nav-ring" href="#how">
      <svg width="80" height="88" viewBox="0 0 80 88"><path d="M40 4 A40 40 0 0 0 24 82" fill="none" stroke="#0792cd" stroke-width="1.6"/><circle cx="44" cy="44" r="36" fill="none" stroke="#fff" stroke-width="1.6"/></svg>
      <span>How</span>
    </a>
    <a class="nav-ring" href="#free-trial">
      <svg width="80" height="88" viewBox="0 0 80 88"><path d="M40 4 A40 40 0 0 0 24 82" fill="none" stroke="#0792cd" stroke-width="1.6"/><circle cx="44" cy="44" r="36" fill="none" stroke="#fff" stroke-width="1.6"/></svg>
      <span>Free Trial</span>
    </a>
  </nav>

  <section class="stats-bar">
    <div class="stat"><span class="stat-value">2.2M</span><span class="stat-label">Photo reviewed last year</span></div>
    <div class="stat"><span class="stat-value">5P</span><span class="stat-label">For per photo reviewed</span></div>
    <div class="stat"><span class="stat-value">97.2%</span><span class="stat-label">Average Compliance</span></div>
    <div class="stat"><span class="stat-value">3-8%</span><span class="stat-label">Sales Increase</span></div>
  </section>
</main>
</body>
</html>
```